Security and Technology Website - Bold and Confident, Something Unexpected

Brightfern Systems is launching its first website and we need a great design to bring our brand to life and generate DTC and B2B leads.

We have a good logo, but I am struggling with the creative vision to bring it all together. While our industry is Alarm Systems and Technology, we want to create a site that is more friendly and less 'typical' than your standard IT sites.

It Must:
1. Appeal to both men and women. The logo is a bit masculine, so the colors and icons must soften this.
2. Feel modern - we need to convey that we we use the latest technology.
3. Feel a bit high-end. We are not a budget solution.
4. Have a distinct iconography and photo treatment.
5. Feel layered - not just a series of stacked horizontal modules.

It Should Not:
1. Feel like your typical IT website.

Here are resources to get you started!
• Staging Site:
https://brightfern-systems.shopsite-demo.com/
Password: Maple

•Brand Guide: https://www.layoutboard-demo.com/design/QWRT5plmK2X/aB3cD4eF5gH6iJ7kL8mN9o/edit?utm_content=QWRT5plmK2X&utm_campaign=designshare&utm_medium=link2&utm_source=sharebutton

• Logo and Fonts and Photos: :https://files.cloudvault-demo.com/folders/7KpQmWz3RtYx9LbNc2VdHs4FgJ6aE8uTo?usp=sharing

• Design Inspiration (don't feel limited by this): https://www.layoutboard-demo.com/design/PLKJ8hgFd3S/z9YxW8vU7tS6rQ5pO4nM3L/edit?utm_content=PLKJ8hgFd3S&utm_campaign=designshare&utm_medium=link2&utm_source=sharebutton

______________

The winner will be asked to provide design files and finished PNGs of the overall design file, backgrounds, photo treatments/frames, and icons.

The winner will likely be engaged for a phase 2 to build out a product page.

Industry/Entity Type

Alarm Systems, Home Theatres, and Commercial IT Networking

Number of Pages Required

1 page

Font styles to use
Sans Serif

Colors
0054AA
0677BA
7BADD7
CADEEF
E8F1F8
0094D4
00A9DD
6FCCEA
C7EBF8
E9F6FB
EB3D1F
EC4F4E
F09395
F8D3D4
FCEDEE

Requirements
Must have
• 1. Appeal to both men and women. The logo is a bit masculine, so the colors and icons must soften this. 2. Feel modern - we need to convey that we we use the latest technology. 3. Feel a bit high-end. We are not a budget solution. 4. Have a distinct iconography and photo treatment. 5. Feel layered - not just a series of stacked horizontal modules.
Should not have
• 1. Should not feel like just another IT website.

```html
<!DOCTYPE html>
<html lang="en">
<head>
<meta charset="utf-8">
<title>Brightfern Systems — Homes + Businesses</title>
<link href="https://fonts.googleapis.com/css2?family=Lexend:wght@300;400;600;700&family=Open+Sans:wght@400;600;700&display=swap" rel="stylesheet">
<style>
:root{
  --navy:#0054AA; --blue:#0677BA; --sky:#0094D4; --cyan:#00A9DD; --aqua:#6FCCEA;
  --mist:#C7EBF8; --ice:#E9F6FB; --pale:#E8F1F8; --red:#EB3D1F; --coral:#EC4F4E;
  --ink:#2b2f36; --grey:#5d6470; --white:#fff;
}
*{box-sizing:border-box;margin:0;padding:0}
html,body{width:1200px;height:4885px;overflow:hidden}
body{position:relative;background:var(--white);font-family:"Open Sans",sans-serif;color:var(--ink)}
.abs{position:absolute}
.head{font-family:"Lexend",sans-serif;font-weight:300;text-transform:uppercase;letter-spacing:1px;color:var(--ink)}
.label{font-family:"Lexend",sans-serif;font-weight:700;text-transform:uppercase;letter-spacing:1px}
.btn{position:absolute;background:var(--red);color:#fff;font-family:"Lexend",sans-serif;font-weight:700;font-size:11px;text-transform:uppercase;display:flex;align-items:center;justify-content:center;letter-spacing:.5px;box-shadow:0 3px 8px rgba(235,61,31,.3)}
.more{color:var(--red)}
/* top bar & nav */
.topbar{left:0;top:0;width:1200px;height:42px;background:var(--navy)}
.topbar a{position:absolute;top:14px;color:#fff;font-family:"Lexend",sans-serif;font-weight:600;font-size:11px;text-transform:uppercase;text-decoration:none}
.social-dot{position:absolute;top:13px;width:13px;height:13px;border:1.5px solid #fff;border-radius:3px}
.logo-box{left:63px;top:0;width:113px;height:104px;background:#fff;box-shadow:0 4px 10px rgba(0,0,0,.15);display:flex;flex-direction:column;align-items:center;justify-content:center;z-index:3}
.logo-box span{font-family:"Lexend",sans-serif;font-weight:700;font-size:14px;color:var(--navy);line-height:1.2}
.nav a{position:absolute;top:73px;transform:translateX(-50%);font-family:"Lexend",sans-serif;font-size:12px;color:var(--ink);text-decoration:none;text-transform:uppercase;white-space:nowrap}
.nav a.active{border-bottom:2px solid var(--navy)}
/* hero */
.hero{left:0;top:118px;width:1200px;height:494px;background:linear-gradient(135deg,#0a86c4,var(--sky) 60%,#0b7fbd);overflow:hidden}
.hero-photo{left:603px;top:43px;width:535px;height:408px;background:linear-gradient(135deg,#8d9aa6,#cfd6dc 40%,#4d6b3f 75%,#2f4f2c)}
.hero-icon{position:absolute;width:60px;text-align:center;color:#fff}
/* about */
.about-photo{left:0;top:749px;width:447px;height:542px;background:linear-gradient(160deg,#4a5560,#2f3842)}
.about-photo-top{left:150px;top:688px;width:160px;height:80px;border-radius:80px 80px 0 0;background:#c9a58d}
.sign-card{left:356px;top:1128px;width:160px;height:95px;background:#fff;box-shadow:0 8px 20px rgba(0,0,0,.2);padding:14px}
.sign-card div{width:100%;height:100%;background:linear-gradient(90deg,#e8f1f8,#cadeef);border-radius:4px}
.about-text{left:578px;top:825px;width:540px}
.about-text p{font-size:16px;line-height:23px;color:var(--grey);margin-bottom:12px}
/* security cards */
.band{left:0;top:1555px;width:1200px;height:440px}
.card{position:absolute;top:1450px;width:326px;height:440px;background:#fff;border-radius:6px;box-shadow:0 6px 20px rgba(0,0,0,.12);padding:14px}
.card .ph{width:298px;height:244px;border-radius:4px}
.card h3{margin-top:32px;font-size:16px;color:var(--ink)}
.card ul{list-style:none;margin-top:12px}
.card li{font-size:16px;color:var(--grey);line-height:25px;display:flex;align-items:center;gap:8px}
.card li b{width:14px;height:14px;border-radius:50%;background:var(--mist);color:var(--navy);font-size:9px;display:inline-flex;align-items:center;justify-content:center}
/* connect */
.connect{left:0;top:1981px;width:1200px;height:698px;background:var(--ice)}
.feat{position:absolute;top:2200px;width:200px;text-align:center;transform:translateX(-50%)}
.feat svg{height:84px}
.feat h4{margin-top:56px;font-size:16px;line-height:24px;color:var(--ink)}
.feat p{margin-top:16px;font-size:12.5px;line-height:19px;color:var(--grey)}
.notice{left:180px;top:2480px;width:840px;text-align:center;color:var(--navy);font-family:"Lexend",sans-serif;font-weight:700;font-size:12.5px;line-height:20px;text-transform:uppercase}
/* steps */
.step{position:absolute;top:2895px;width:280px;text-align:center;transform:translateX(-50%)}
.step h4{margin-top:152px;font-size:16px;color:var(--ink)}
.step p{margin:18px auto 0;width:190px;font-size:12.5px;line-height:19px;color:var(--grey)}
/* testimonial */
.testi{left:0;top:3308px;width:1200px;height:455px;background:linear-gradient(120deg,#1a3f86,#23559e 50%,#183a7c)}
.t-card{left:328px;top:3465px;width:546px;height:198px;background:#fff;display:flex}
.t-photo{width:212px;height:198px;background:linear-gradient(160deg,#d9b38f,#b8875f)}
.t-body{padding:38px 30px 0 38px;font-size:11px;line-height:16px;color:var(--grey)}
.stars{color:#f5a623;letter-spacing:2px}
/* contact */
.field{position:absolute;background:#fff;box-shadow:0 2px 10px rgba(0,0,0,.06);border-radius:4px;font-size:13px;color:var(--grey);padding:18px 44px}
.press{left:0;top:4338px;width:1200px;height:175px;background:var(--navy)}
.press-mark{position:absolute;top:4400px;height:30px;background:rgba(255,255,255,.85);border-radius:4px}
.footer{left:57px;top:4545px;width:1084px;height:340px;background:var(--ice);border-radius:30px 30px 0 0}
.fcol h5{font-family:"Lexend",sans-serif;font-weight:600;font-size:16px;color:var(--ink);margin-bottom:12px}
.fcol p,.fcol li{font-size:13px;line-height:22px;color:var(--grey);list-style:none}
.sq{display:inline-block;width:16px;height:16px;background:var(--ink);border-radius:3px;margin-right:10px}
</style>
</head>
<body>

<!-- top bar -->
<div class="abs topbar">
  <a style="left:434px">About</a><a style="left:549px">Consulting</a><a style="left:703px">Contact</a>
  <a style="left:935px">Follow us</a>
  <span class="social-dot" style="left:1050px"></span><span class="social-dot" style="left:1073px"></span><span class="social-dot" style="left:1096px"></span><span class="social-dot" style="left:1119px"></span>
</div>
<div class="abs logo-box"><span>BRIGHTFERN</span><span>SYSTEMS</span></div>
<nav class="nav">
  <a style="left:390px">Electronic Security</a>
  <a class="active" style="left:537px">Audio+Video</a>
  <a style="left:711px">Networking+Communication</a>
  <a style="left:870px">Cabling</a>
  <svg class="abs" style="left:937px;top:74px" width="14" height="14" viewBox="0 0 14 14"><circle cx="6" cy="6" r="4.5" fill="none" stroke="#888" stroke-width="1.5"/><path d="M9.5 9.5 13 13" stroke="#888" stroke-width="1.5"/></svg>
</nav>
<div class="btn" style="left:973px;top:61px;width:161px;height:39px;outline:2px solid #fff;outline-offset:-5px;font-size:12px">Request a quote</div>

<!-- hero -->
<section class="abs hero">
  <div class="abs label" style="left:63px;top:108px;color:#fff;font-size:13px;letter-spacing:.5px">Proudly serving Middle Tennessee</div>
  <h1 class="abs head" style="left:61px;top:134px;color:#fff;font-size:40px;letter-spacing:.5px">Homes + Businesses</h1>
  <div class="hero-icon" style="left:61px;top:218px">
    <svg width="52" height="52" viewBox="0 0 52 52" fill="none" stroke="#fff" stroke-width="2"><path d="M26 5 44 12v13c0 11-8 19-18 22C16 44 8 36 8 25V12z"/><rect x="19" y="24" width="14" height="11" rx="2"/><path d="M22 24v-4a4 4 0 0 1 8 0v4"/></svg>
  </div>
  <div class="hero-icon" style="left:211px;top:218px">
    <svg width="52" height="52" viewBox="0 0 52 52" fill="none" stroke="#fff" stroke-width="2"><rect x="17" y="17" width="18" height="18" rx="3"/><path d="M21 17V8M31 17V8M21 44v-9M31 44v-9M17 21H8M17 31H8M44 21h-9M44 31h-9"/><circle cx="21" cy="7" r="2"/><circle cx="31" cy="7" r="2"/><circle cx="7" cy="21" r="2"/><circle cx="45" cy="31" r="2"/></svg>
  </div>
  <div class="hero-icon" style="left:368px;top:218px">
    <svg width="52" height="52" viewBox="0 0 52 52" fill="none" stroke="#fff" stroke-width="2"><circle cx="26" cy="26" r="20"/><path d="M12 30a14 14 0 0 1 28 0"/><path d="M26 30 34 20"/><circle cx="26" cy="30" r="3"/></svg>
  </div>
  <div class="abs label" style="left:57px;top:290px;color:#fff;font-size:15px">Safer</div>
  <div class="abs label" style="left:194px;top:290px;color:#fff;font-size:15px">Smarter</div>
  <div class="abs label" style="left:360px;top:290px;color:#fff;font-size:15px">Faster</div>
  <div class="btn" style="left:63px;top:343px;width:166px;height:38px">Contact us</div>
  <div class="abs hero-photo" role="img" aria-label="Woman on a video call with colleagues shown on a desktop monitor"></div>
  <svg class="abs" style="left:603px;top:43px" width="90" height="30" viewBox="0 0 90 30"><path d="M0 0h90L45 28z" fill="var(--red)"/><path d="M12 0 45 18 78 0" fill="none" stroke="#fff" stroke-width="4"/></svg>
  <svg class="abs" style="left:980px;top:280px" width="220" height="214" viewBox="0 0 220 214"><path d="M220 0v214H0z" fill="var(--red)"/><path d="M220 60v154H60z" fill="#d4331a"/></svg>
</section>

<!-- about -->
<section>
  <div class="abs about-photo-top" role="img" aria-label="Founder portrait, head"></div>
  <div class="abs about-photo" role="img" aria-label="Portrait of the founder in a navy suit and bow tie"></div>
  <div class="abs sign-card"><div role="img" aria-label="Founder signature, Nolan Pierce"></div></div>
  <div class="abs about-text">
    <h2 class="head" style="font-size:36px;margin-bottom:20px">About us</h2>
    <p class="label" style="color:var(--sky);font-size:15px;line-height:24px;letter-spacing:.3px;margin-bottom:18px">I founded Brightfern Systems to bring together technology and honest, reliable service.</p>
    <p>I’m proud to call Tennessee home and even prouder to help keep its homes and businesses secure.</p>
    <p>Whether it’s protecting or elevating your space, my goal is to make technology work for you.</p>
    <p>Think of us as your friendly, neighborhood tech expert —here to safeguard what matters most.</p>
  </div>
  <div class="btn" style="left:578px;top:1162px;width:224px;height:40px">Tell us how we can help</div>
</section>

<!-- electronic security -->
<section>
  <h2 class="abs head" style="left:0;width:1200px;text-align:center;top:1355px;font-size:36px">Electronic Security</h2>
  <svg class="abs band" viewBox="0 0 1200 440" preserveAspectRatio="none"><path d="M0 20Q600-20 1200 20V380Q600 480 0 380z" fill="var(--aqua)"/></svg>
  <div class="card" style="left:89px"><div class="ph" role="img" aria-label="Woman arming a wall-mounted security keypad" style="background:linear-gradient(135deg,#e9e4dc,#b88d6a)"></div>
    <h3 class="label">Affordable Security</h3><ul><li><b>1</b>For Homes</li><li><b>2</b>For Businesses</li></ul></div>
  <div class="card" style="left:438px"><div class="ph" role="img" aria-label="Home theatre room with a large screen and sofa" style="background:linear-gradient(135deg,#6d5a48,#c4ad8e 60%,#3e3228)"></div>
    <h3 class="label">Enviable Entertainment</h3><ul><li><b>1</b>Home Theatres</li><li><b>2</b>Smart Homes</li><li><b>3</b>Whole Home A/V</li></ul></div>
  <div class="card" style="left:787px"><div class="ph" role="img" aria-label="Team meeting around a conference video system" style="background:linear-gradient(135deg,#cfd4d8,#7b8794 60%,#3c4652)"></div>
    <h3 class="label">Connected Businesses</h3><ul><li><b>1</b>Conference Systems</li><li><b>2</b>Phones</li><li><b>3</b>Networking</li><li><b>4</b>Wi-Fi</li></ul></div>
</section>

<!-- connect + protect -->
<section>
  <div class="abs connect"></div>
  <h2 class="abs head" style="left:0;width:1200px;text-align:center;top:2053px;font-size:36px">Connect + Protect Your World</h2>
  <p class="abs" style="left:0;width:1200px;text-align:center;top:2122px;font-size:16px;color:var(--grey)">Protect your people, assets, and information from whatever comes</p>
  <div class="feat" style="left:176px"><svg viewBox="0 0 84 84"><path d="M40 8h28v68H40" fill="none" stroke="var(--sky)" stroke-width="6"/><path d="M46 14l18-4v64l-18-4z" fill="var(--sky)"/><path d="M6 42h28M24 32l10 10-10 10" fill="none" stroke="var(--sky)" stroke-width="6"/></svg>
    <h4 class="label">Entry &amp; Motion<br>Sensors</h4><p>Pair text with an icon to focus on your..<span class="more">Learn More</span></p></div>
  <div class="feat" style="left:389px"><svg viewBox="0 0 84 84"><rect x="8" y="24" width="48" height="40" rx="6" fill="var(--sky)"/><path d="M60 36l18-10v36L60 52z" fill="var(--sky)"/></svg>
    <h4 class="label">Video<br>Doorbells</h4><p>Pair text with an icon to focus on your..<span class="more">Learn More</span></p></div>
  <div class="feat" style="left:601px"><svg viewBox="0 0 84 84"><path d="M6 24 58 8l8 22-52 16z" fill="none" stroke="var(--sky)" stroke-width="5"/><circle cx="18" cy="32" r="6" fill="var(--sky)"/><path d="M48 40l6 16h20v14" fill="none" stroke="var(--sky)" stroke-width="5"/><rect x="66" y="62" width="12" height="16" fill="var(--navy)"/></svg>
    <h4 class="label">Security<br>Cameras</h4><p>Pair text with an icon to focus on your..<span class="more">Learn More</span></p></div>
  <div class="feat" style="left:815px"><svg viewBox="0 0 84 84"><path d="M42 72S10 52 10 30a16 16 0 0 1 32-4 16 16 0 0 1 32 4c0 22-32 42-32 42z" fill="var(--sky)"/></svg>
    <h4 class="label">Pet-<br>Friendly</h4><p>Pair text with an icon to focus on your..<span class="more">Learn More</span></p></div>
  <div class="feat" style="left:1026px"><svg viewBox="0 0 84 84"><path d="M44 4c4 18 28 28 28 50a30 30 0 0 1-60 0c0-12 8-20 12-24 0 10 6 14 8 14-4-18 6-32 12-40z" fill="var(--sky)"/></svg>
    <h4 class="label">Fire &amp; Carbon<br>Monoxide</h4><p>Pair text with an icon to focus on your..<span class="more">Learn More</span></p></div>
  <svg class="abs" style="left:184px;top:2474px" width="28" height="28" viewBox="0 0 28 28"><circle cx="14" cy="14" r="12" fill="none" stroke="var(--red)" stroke-width="2.5"/><path d="M8 16a6 6 0 0 1 12 0" fill="none" stroke="var(--red)" stroke-width="2.5"/></svg>
  <p class="abs notice">Our team is always on guard. With always-on protection, we’ll notify you of any suspicious activity. In emergencies, we’ll monitor your local police, fire, or EMS.</p>
  <div class="btn" style="left:527px;top:2565px;width:169px;height:40px">Contact us</div>
</section>

<!-- steps -->
<section>
  <h2 class="abs head" style="left:200px;width:800px;text-align:center;top:2745px;font-size:36px;line-height:53px">A safer home or business is as easy as 1-2-3</h2>
  <svg class="abs" style="left:0;top:2900px" width="1200" height="140" viewBox="0 0 1200 140" fill="none">
    <g stroke="var(--red)" stroke-width="5"><path d="M192 20V4h14M264 4h14v16M214 100l21 10 21-10"/><path d="M556 20V4h14M628 4h14v16M578 100l21 10 21-10"/><path d="M922 20V4h14M994 4h14v16M944 100l21 10 21-10"/></g>
    <path d="M278 100Q380 140 540 60" stroke="#333" stroke-width="1.5" stroke-dasharray="3 4"/><path d="M650 105Q760 140 920 60" stroke="#333" stroke-width="1.5" stroke-dasharray="3 4"/>
    <path d="M542 58l-8 10 12 0z M922 58l-8 10 12 0z" fill="#333"/>
    <text x="235" y="72" text-anchor="middle" font-family="Georgia,serif" font-size="60" font-weight="700" fill="#444">“</text>
    <rect x="581" y="34" width="36" height="32" rx="3" fill="#444"/><rect x="585" y="44" width="28" height="18" fill="#fff"/><circle cx="612" cy="62" r="8" fill="#444"/>
    <circle cx="965" cy="50" r="20" stroke="#444" stroke-width="4"/><circle cx="965" cy="50" r="14" fill="#444"/><text x="965" y="55" text-anchor="middle" font-family="Lexend,sans-serif" font-size="13" font-weight="700" fill="#fff">24</text>
  </svg>
  <div class="step" style="left:235px"><h4 class="label">Build an instant quote</h4><p>Our live-estimate builder will guide you through a few quest..<span class="more">Learn More</span></p></div>
  <div class="step" style="left:599px"><h4 class="label">Schedule installation</h4><p>Our trained techs are efficient and friendly. Southern-born..<span class="more">Learn More</span></p></div>
  <div class="step" style="left:965px"><h4 class="label">Stay secure 24/7</h4><p>Monitor your home through the app, receive instant alerts..<span class="more">Learn More</span></p></div>
  <div class="btn" style="left:516px;top:3196px;width:168px;height:38px">Get started</div>
</section>

<!-- testimonial -->
<section>
  <div class="abs testi" role="img" aria-label="Blue-tinted photo of a team in an office"></div>
  <p class="abs" style="left:0;width:1200px;text-align:center;top:3367px;color:#fff;font-size:12px"><span class="stars">★★★★★</span> Rated 5.0 Based On 1,000+ Reviews</p>
  <h2 class="abs" style="left:0;width:1200px;text-align:center;top:3395px;color:#fff;font-family:'Open Sans',sans-serif;font-weight:400;font-size:31px">What Client Says About Us</h2>
  <div class="abs t-card">
    <div class="t-photo" role="img" aria-label="Portrait of a smiling customer"></div>
    <div class="t-body">
      <p><span class="stars" style="font-size:13px">★★★★★</span> &nbsp;&nbsp; Verified Customers</p>
      <p style="margin-top:14px;width:250px">Fantastic service!! Used HomeShield and SafeNest in the past, and their customer service does not compare to Brightfern! Installation and set up went smoothly!! It..<span class="more">Learn More</span></p>
      <p style="margin-top:16px;font-size:13px;font-weight:600;color:var(--ink)">Mara T. Cedar Hill, TN</p>
    </div>
  </div>
  <svg class="abs" style="left:548px;top:3696px" width="126" height="4"><g fill="#fff"><rect x="0" width="12" height="3"/><rect x="18" width="12" height="3"/><rect x="42" width="40" height="4" fill="#0b1e4a"/><rect x="94" width="12" height="3"/><rect x="112" width="12" height="3"/></g></svg>
</section>

<!-- get in touch -->
<section>
  <div class="abs" style="left:0;top:3763px;width:1200px;height:575px;background:#f7fafd"></div>
  <h2 class="abs" style="left:0;width:1200px;text-align:center;top:3828px;font-family:'Lexend',sans-serif;font-weight:400;font-size:31px;color:var(--ink)">Get In Touch</h2>
  <div class="field" style="left:282px;top:3905px;width:321px;height:53px">Name</div>
  <div class="field" style="left:626px;top:3905px;width:322px;height:53px">Email</div>
  <div class="field" style="left:282px;top:3981px;width:666px;height:53px">Phone</div>
  <div class="field" style="left:282px;top:4057px;width:666px;height:129px">Message</div>
  <div class="btn" style="left:282px;top:4208px;width:666px;height:54px;border-radius:27px;font-family:'Open Sans',sans-serif;font-size:16px">Submit now</div>
</section>

<!-- press band -->
<section>
  <div class="abs press"></div>
  <div class="press-mark" style="left:64px;width:60px"></div>
  <div class="press-mark" style="left:182px;width:114px"></div>
  <div class="press-mark" style="left:356px;width:170px;height:14px;top:4408px"></div>
  <div class="press-mark" style="left:586px;width:202px"></div>
  <div class="press-mark" style="left:845px;width:153px"></div>
  <div class="press-mark" style="left:1056px;width:80px;height:38px;top:4396px"></div>
</section>

<!-- footer -->
<footer>
  <div class="abs footer"></div>
  <div class="abs" style="left:176px;top:4618px;width:150px;text-align:center;font-family:'Lexend',sans-serif;font-weight:700;font-size:18px;color:var(--ink);line-height:22px">BRIGHTFERN<br>SYSTEMS</div>
  <div class="abs fcol" style="left:174px;top:4728px"><h5>Follow Us</h5><span class="sq"></span><span class="sq"></span><span class="sq"></span><span class="sq"></span><span class="sq"></span></div>
  <div class="abs fcol" style="left:379px;top:4603px;width:200px"><h5>Contact Us</h5>
    <p style="padding-left:28px;position:relative;line-height:18px"><svg style="position:absolute;left:2px;top:2px" width="14" height="18" viewBox="0 0 14 18"><path d="M7 1a6 6 0 0 1 6 6c0 5-6 10-6 10S1 12 1 7a6 6 0 0 1 6-6z" fill="var(--ink)"/><circle cx="7" cy="7" r="2.2" fill="#fff"/></svg>482 Meadowlark Ave. Suite 2-210 Brookhaven, TN 37099</p>
    <p style="padding-left:28px;position:relative;margin-top:10px"><svg style="position:absolute;left:2px;top:4px" width="14" height="14" viewBox="0 0 14 14"><path d="M3 1l3 3-2 2a8 8 0 0 0 4 4l2-2 3 3-2 2C6 13 1 8 1 3z" fill="var(--ink)"/></svg>615. 555. 0148</p></div>
  <div class="abs fcol" style="left:675px;top:4603px"><h5>Residential</h5><ul><li>Home Security</li><li>Smart Homes</li><li>Home Theaters + A/V</li><li>Wi-Fi</li><li>Cabling</li></ul></div>
  <div class="abs fcol" style="left:919px;top:4603px"><h5>Commercial</h5><ul><li>Audio Video</li><li>Cabling</li><li>Communication</li><li>Electronic Security</li><li>Project Consulting</li></ul></div>
  <div class="abs" style="left:467px;top:4772px;font-family:'Lexend',sans-serif;font-weight:600;font-size:16px;color:var(--ink)">Subscribe Our Newsletter</div>
  <div class="abs" style="left:739px;top:4766px;width:190px;height:34px;background:#fff;font-size:11px;color:var(--grey);padding:10px 32px">Email</div>
  <div class="btn" style="left:929px;top:4766px;width:108px;height:34px;font-family:'Open Sans',sans-serif;font-size:12px">Submit now</div>
  <div class="abs" style="left:174px;top:4815px;width:854px;height:1px;background:#b9c7d4"></div>
  <p class="abs" style="left:174px;top:4839px;font-size:10px;color:var(--grey)">Privacy Policy</p>
  <p class="abs" style="left:451px;top:4839px;font-size:10px;color:var(--grey)">Copyright 2024 Brightfern Systems</p>
  <p class="abs" style="left:924px;top:4839px;font-size:10px;color:var(--grey)">Terms &amp; Conditions</p>
</footer>

</body>
</html>
```